Flyer Design Project

I teach a spiritual dance class and I want to explain what it is and who it would benefit. I would love to have a sticker for where I am teaching it because that can change.

I want it to be a bit spiritual, very hip and cool, and transformational!!

Target Market(s)

Mostly women (or enlightened men)! all ages

Requirements
Must have
• Tidal Sway

We need to move. We need to breathe. We need to smile and giggle and laugh and cry and scream and make noise and dance. It's not about burning calories and it is not about reaching a goal. It's about feeling. It's about taking the time to nurture our souls. It's about finding joy and peace in our hectic lives. It's about healing.

Tidal Sway is a wildly fun, uplifting, emotionally cleansing, refreshing, restorative, heart-opening, transformational dance celebration that is sure to leave you relaxed and smiling. All ages, shapes and sizes are welcome with no experience necessary.
About Nora:

I was certified at Venduro in both “Move Through Morning” and “Orbit Motion” and am a
certified Group Exercise Instructor with the Cardio and Wellness Guild of Northland (CWGN). I also have a black belt in Tae Kwon Do. As of 2013, I will be a certified holistic health and nutrition coach and am the creator of the popular Bright, Brisk, and Bold page on Chatterbook.
For more info:
Noradekker@mailquill.com

Classes and workshops to energize your body, mind, and spirit.

```html
<!DOCTYPE html>
<html lang="en">
<head>
<meta charset="utf-8">
<title>Tidal Sway – Dance Class Flyer</title>
<link rel="stylesheet" href="https://fonts.googleapis.com/css2?family=Alfa+Slab+One&family=Archivo+Black&family=Bangers&family=Bungee&family=Coustard:wght@400;900&family=Great+Vibes&family=Libre+Baskerville&family=Open+Sans:wght@400;700;800&family=Poiret+One&display=swap">
<style>
  :root {
    --ink: #141414;
    --purple: #7a2fd6;
    --soul-purple: #8a3fe0;
    --green: #34a84c;
    --paper: #ffffff;
    --sky-top: #3d6fc6;
    --sky-mid: #86a9dd;
    --glow-peach: #f3c19a;
    --glow-orange: #f2a142;
    --dusk-coral: #e8a27a;
    --dusk-lilac: #aaa4da;
    --dusk-base: #bdb8ee;
  }
  * { margin: 0; padding: 0; box-sizing: border-box; }
  html, body { width: 1200px; height: 900px; overflow: hidden; background: var(--paper); }
  .flyer {
    position: absolute; left: 284px; top: 0; width: 704px; height: 900px; overflow: hidden;
    color: var(--ink); font-family: "Open Sans", Arial, sans-serif;
  }
  .flyer-backdrop {
    position: absolute; inset: 0;
    background: linear-gradient(180deg, var(--sky-top) 0%, var(--sky-mid) 24%, var(--glow-peach) 44%, var(--glow-orange) 56%, var(--dusk-coral) 64%, var(--dusk-lilac) 80%, var(--dusk-base) 100%);
  }
  .line { position: absolute; white-space: nowrap; line-height: 1; }

  .mantra-move { left: 142px; top: 14px; font-size: 22px; }
  .mantra-move .big-move { font-family: "Alfa Slab One", serif; font-size: 46px; }
  .mantra-move .script { font-family: "Great Vibes", cursive; font-size: 40px; }

  .mantra-smile { left: 216px; top: 58px; }
  .mantra-smile .smile { font-family: "Coustard", serif; font-size: 58px; }
  .mantra-smile .amp { font-family: "Libre Baskerville", serif; font-size: 20px; vertical-align: top; }
  .mantra-smile .giggle { font-family: "Alfa Slab One", serif; font-size: 62px; letter-spacing: 2px; }

  .mantra-laugh { left: 200px; top: 118px; font-family: "Libre Baskerville", serif; }
  .mantra-laugh .laugh { font-size: 68px; }
  .mantra-laugh .amp { font-size: 20px; }
  .mantra-laugh .scream { font-size: 50px; }
  .mantra-cry { left: 366px; top: 170px; font-family: "Archivo Black", sans-serif; font-size: 42px; }

  .mantra-dance {
    left: 140px; top: 222px; font-family: "Bangers", cursive; font-size: 76px; color: var(--purple);
    letter-spacing: 0; transform: scaleX(0.95); transform-origin: left top;
  }

  .statement { font-weight: 800; font-size: 19px; }
  .statement-calories { left: 230px; top: 314px; }
  .statement-goal { left: 230px; top: 351px; }
  .statement-feeling { left: 230px; top: 390px; }
  .statement-feeling .feeling { font-family: "Bungee", sans-serif; font-weight: 400; font-size: 46px; color: var(--green); letter-spacing: 1px; }
  .statement-time { left: 230px; top: 440px; }
  .statement-time .time { font-family: "Archivo Black", sans-serif; font-weight: 400; font-size: 54px; }
  .statement-souls { left: 230px; top: 484px; }
  .statement-souls .souls {
    display: inline-block; font-family: "Poiret One", sans-serif; font-weight: 400; font-size: 76px;
    color: var(--soul-purple); transform: scaleX(0.7); transform-origin: left bottom;
  }

  .class-name { left: 8px; top: 588px; font-family: "Bangers", cursive; font-size: 78px; letter-spacing: 2px; }
  .intro { font-size: 20px; line-height: 1.35; }
  .intro-right { left: 410px; top: 610px; }
  .intro-body { left: 8px; top: 664px; }
  .class-info-label { left: 8px; top: 722px; font-weight: 800; font-size: 19px; }

  .location-sticker { position: absolute; left: 0; top: 744px; width: 367px; height: 156px; background: var(--paper); }

  .contact { left: 378px; top: 786px; font-weight: 800; font-size: 22px; line-height: 1.6; }
</style>
</head>
<body>
  <main class="flyer">
    <div class="flyer-backdrop" role="img" aria-label="Sunset sky over the sea with a silhouetted woman leaping in dance, arms raised"></div>

    <p class="line mantra-move">We need to <span class="big-move">MOVE.</span> We need to <span class="script">Breathe</span></p>
    <p class="line mantra-smile"><span class="smile">Smile</span><span class="amp">&amp;</span><span class="giggle">GIGGLE</span></p>
    <p class="line mantra-laugh"><span class="laugh">Laugh</span> <span class="amp">&amp;</span> <span class="scream">SCREAM</span></p>
    <p class="line mantra-cry">CRY</p>
    <h1 class="line mantra-dance">DANCE &amp; MAKE NOISE!</h1>

    <p class="line statement statement-calories">It is not about burning calories.</p>
    <p class="line statement statement-goal">It is not about reaching a goal.</p>
    <p class="line statement statement-feeling">It's about <span class="feeling">FEELING</span></p>
    <p class="line statement statement-time">It's about taking the <span class="time">TIME</span></p>
    <p class="line statement statement-souls">To nurture our <span class="souls">SOULS</span></p>

    <h2 class="line class-name">TIDAL SWAY</h2>
    <p class="line intro intro-right">Is a wildly fun, uplifting,<br>Emotionally cleansing,</p>
    <p class="line intro intro-body">Refreshing, restorative, heart-opening, transformational dance<br>experience that is sure to leave you relaxed and smiling!</p>
    <p class="line class-info-label">CLASS INFORMATION</p>

    <div class="location-sticker"></div>

    <p class="line contact">For more info:<br>Noradekker@mailquill.com</p>
  </main>
</body>
</html>
```